Business Card Design Project

Tarvolink - based in Melbourne, Australia. We plan, design, implement and support network infrastructure (Plemba, Hollvask, Q8, Stormpike etc).

Target Market(s)

Small/Medium enterprise and Corporate.

Industry/Entity Type

Business

```html
<!DOCTYPE html>
<html lang="en">
<head>
<meta charset="utf-8">
<title>Tarvolink Business Card</title>
<link rel="stylesheet" href="https://fonts.googleapis.com/css2?family=Arimo:wght@400;700&display=swap">
<style>
  :root {
    --backdrop: #e6e5e2;
    --card: #ffffff;
    --orange: #f7941d;
    --orange-soft: #fbc98a;
    --ink: #3a3a3a;
    --ink-muted: #6a6a6a;
    --accent-text: #d9780f;
  }
  * { margin: 0; padding: 0; box-sizing: border-box; }
  html, body {
    width: 1200px; height: 752px; overflow: hidden;
    background: var(--backdrop);
    font-family: "Arimo", Arial, sans-serif;
  }
  .stage {
    position: relative; width: 1200px; height: 752px;
    display: flex; align-items: center; justify-content: center; gap: 60px;
  }
  .card {
    position: relative; width: 500px; height: 286px;
    background: var(--card);
    box-shadow: 0 6px 18px rgba(0,0,0,0.12);
    overflow: hidden;
  }
  /* Front */
  .card--front {
    background: radial-gradient(ellipse 62% 70% at 50% 50%, var(--orange) 0%, var(--orange-soft) 45%, var(--card) 85%);
    display: flex; align-items: center; justify-content: center;
  }
  .brand { display: flex; align-items: center; gap: 12px; }
  .brand__dot { width: 44px; height: 44px; border-radius: 50%; background: var(--ink-muted); }
  .brand__name { font-size: 46px; font-weight: 700; color: var(--ink-muted); letter-spacing: 0.5px; }
  /* Back */
  .card--back .band {
    position: absolute; left: 0; right: 0; bottom: 0; height: 78px;
    background: linear-gradient(90deg, var(--orange) 0%, var(--orange) 30%, var(--orange-soft) 65%, var(--card) 100%);
  }
  .contact-lines {
    position: absolute; left: 22px; top: 22px;
    font-size: 13px; line-height: 1.45; color: var(--ink);
  }
  .person {
    position: absolute; right: 24px; top: 22px; text-align: right;
    font-size: 13px; line-height: 1.45; color: var(--ink);
  }
  .person__name { font-size: 19px; color: var(--accent-text); }
  .person__role { font-size: 13px; color: var(--accent-text); margin-bottom: 14px; }
  .website {
    position: absolute; left: 22px; bottom: 86px;
    font-size: 12px; color: var(--ink);
  }
  .brand--small {
    position: absolute; left: 22px; bottom: 24px; gap: 7px;
  }
  .brand--small .brand__dot { width: 24px; height: 24px; background: var(--card); }
  .brand--small .brand__name { font-size: 24px; color: var(--card); }
</style>
</head>
<body>
  <main class="stage">
    <section class="card card--front" aria-label="Card front">
      <div class="brand">
        <span class="brand__dot"></span>
        <span class="brand__name">Tarvolink</span>
      </div>
    </section>

    <section class="card card--back" aria-label="Card back">
      <div class="contact-lines">
        <p>Office: 0400-318-275</p>
        <p>Fax: 0400-318-276</p>
      </div>
      <div class="person">
        <p class="person__name">Marten Soller</p>
        <p class="person__role">Manager</p>
        <p>Melbourne, Australia</p>
        <p>m.soller@tarvolink.au</p>
      </div>
      <p class="website">www.tarvolink.au</p>
      <div class="band"></div>
      <div class="brand brand--small">
        <span class="brand__dot"></span>
        <span class="brand__name">Tarvolink</span>
      </div>
    </section>
  </main>
</body>
</html>
```